Technology Solutions Provider

Let’s design a business card that will be as simple and bold at the same time. Name, email address, website & phone number.

Target Market(s)

Small to Medium Size Business

Industry/Entity Type

It Professional

Contact Information for Business Card

Name, email, website, phone numbers

Font styles to use
Sans Serif

Colors
ec1f27
f04a50
dddddd
919191
000000
ffffff

Requirements
Must have
• Clean simple look using my existing logo. I just need to the basic contact information on this card.
Nice to have
• Im considering the square size card versus the standard size business card.
Should not have
• No Mailing Address, no list of services.

```html
<!DOCTYPE html>
<html lang="en">
<head>
<meta charset="utf-8">
<title>kernelpath business card</title>
<link href="https://fonts.googleapis.com/css2?family=Open+Sans:wght@400;700&family=Tinos&display=swap" rel="stylesheet">
<style>
  :root{
    --red:#ec1f27;
    --red-soft:#f04a50;
    --light:#dddddd;
    --mid:#919191;
    --black:#000000;
    --white:#ffffff;
    --stage:#e9e9e9;
  }
  *{margin:0;padding:0;box-sizing:border-box}
  html,body{width:1200px;height:904px;overflow:hidden;background:var(--stage)}
  body{display:flex;align-items:center;justify-content:center;gap:80px;font-family:"Open Sans",sans-serif}
  .card{width:480px;height:480px;position:relative;background:var(--white);box-shadow:0 6px 18px rgba(0,0,0,.15);overflow:hidden}
  .card-front{display:flex;align-items:center;justify-content:center}
  .brand{display:flex;flex-direction:column;align-items:flex-start}
  .brand-name{font-size:50px;font-weight:400;color:var(--black);letter-spacing:1px;line-height:1}
  .brand-tagline{font-family:"Tinos",serif;font-size:17px;color:var(--mid);margin-top:4px;letter-spacing:.5px}
  .contact-band{position:absolute;left:0;right:0;top:200px;bottom:0;background:var(--black)}
  .mark-area{position:absolute;right:0;top:120px;width:150px;height:360px;background:linear-gradient(180deg,var(--light),#c9c9c9)}
  .identity{position:absolute;left:60px;top:120px}
  .person-name{font-size:26px;font-weight:700;color:var(--red);line-height:1.1}
  .person-role{font-size:17px;color:var(--black)}
  .contacts{position:absolute;left:80px;top:300px;list-style:none}
  .contacts li{display:flex;align-items:center;gap:16px;color:var(--white);font-size:17px;height:28px;white-space:nowrap}
  .contacts svg{width:16px;height:16px;flex:none}
</style>
</head>
<body>
  <section class="card card-front">
    <div class="brand">
      <span class="brand-name">kernelpath</span>
      <span class="brand-tagline">technology solutions provider</span>
    </div>
  </section>

  <section class="card card-back">
    <div class="contact-band"></div>
    <div class="mark-area" role="img" aria-label="Area for the brand's decorative mark"></div>
    <div class="identity">
      <p class="person-name">Dana Reyes</p>
      <p class="person-role">Manager</p>
    </div>
    <ul class="contacts">
      <li><svg viewBox="0 0 16 16"><path d="M4 2l3 3-2 2a9 9 0 0 0 4 4l2-2 3 3-2 2C7 14 2 9 2 4z" fill="var(--red)"/></svg>+100 555 0142</li>
      <li><svg viewBox="0 0 16 16"><rect x="1" y="3" width="14" height="10" rx="1" fill="var(--red)"/><path d="M1 4l7 5 7-5" stroke="var(--black)" stroke-width="1.2" fill="none"/></svg>hello@kernelpath.net</li>
      <li><svg viewBox="0 0 16 16"><circle cx="8" cy="8" r="6.5" fill="none" stroke="var(--red)" stroke-width="1.5"/><path d="M1.5 8h13M8 1.5c-3 3-3 10 0 13M8 1.5c3 3 3 10 0 13" stroke="var(--red)" stroke-width="1.2" fill="none"/></svg>www.kernelpath.net</li>
    </ul>
  </section>
</body>
</html>
```